Marketing Graphics for App

We need a feature graphic to be used in an app store listing for the app Quill Puzzles Plus. Quill Puzzles Plus is a brain training app that allows people to practice various cognitive skills. Our immediate need is for a graphic that can be scaled to run on the Verano Shop Hub free app of the day promotion. This ad will show up on the lock screen on the Tolvo Slate that users will see when the Tolvo Slate is turned on before it is unlocked.

We need a layered PSD file, so that internal elements can be scaled/moved. Please see the guidelines for the graphics ads from Verano.

Concept style guide: https://media-cdn.verano-example.com/docs/ads/VeranoLockCreativeRules.pdf

Technical style guide: https://media-cdn.verano-example.com/docs/ads/VeranoTolvoSlateAdGuide.pdf

I have included some of our existing graphics assets.

See also the app store listing:
http://www.verano-example.com/shop/item/Q77RTWPLMN

Target Market(s)

Mobile phone app users.

Industry/Entity Type

Training

Requirements
Must have
• Text: Quill Puzzles Plus

Text: Exercise Your Brain
Possibly add: Brain Training Games

```html
<!DOCTYPE html>
<html lang="en">
<head>
<meta charset="utf-8">
<title>Quill Puzzles Plus – Lock Screen Feature Graphic</title>
<link rel="stylesheet" href="https://fonts.googleapis.com/css2?family=Lato:wght@700;900&display=swap">
<style>
  :root {
    --page-bg: #eef0f3;
    --ad-blue: #034a96;
    --emblem-tint: #2b64a6;
    --title-white: #ffffff;
    --tagline-grey: #8ea2c6;
    --control-dark: #2e2e2e;
    --control-mid: #555555;
    --knob-grey: #6b6b6b;
    --icon-light: #d9d9d9;
  }
  * { margin: 0; padding: 0; box-sizing: border-box; }
  html, body {
    width: 1200px;
    height: 1200px;
    overflow: hidden;
    background: var(--page-bg);
  }
  .canvas {
    position: relative;
    width: 1200px;
    height: 1200px;
  }
  .lock-ad {
    position: absolute;
    left: 243px;
    top: 53px;
    width: 714px;
    height: 1094px;
    background: var(--ad-blue);
    overflow: hidden;
    font-family: "Lato", Arial, sans-serif;
  }
  .app-emblem {
    position: absolute;
    left: 200px;
    top: 231px;
    width: 314px;
    height: 340px;
    border-radius: 40px;
    background: var(--emblem-tint);
  }
  .app-title {
    position: absolute;
    left: 0;
    width: 100%;
    top: 700px;
    text-align: center;
    color: var(--title-white);
    font-size: 51px;
    font-weight: 700;
    line-height: 1;
    white-space: nowrap;
  }
  .app-tagline {
    position: absolute;
    left: 0;
    width: 100%;
    top: 776px;
    text-align: center;
    color: var(--tagline-grey);
    font-size: 23px;
    font-weight: 900;
    letter-spacing: 0.5px;
    line-height: 1;
    white-space: nowrap;
  }
  .start-button {
    position: absolute;
    left: 0;
    top: 870px;
    width: 184px;
    height: 102px;
    border-radius: 0 51px 51px 0;
    background: linear-gradient(180deg, var(--control-mid), var(--control-dark));
    color: var(--title-white);
    font-size: 19px;
    font-weight: 900;
    display: flex;
    align-items: center;
    padding-left: 39px;
    white-space: nowrap;
  }
  .unlock-slider {
    position: absolute;
    right: 0;
    top: 870px;
    width: 181px;
    height: 102px;
    border-radius: 51px 0 0 51px;
    background: linear-gradient(180deg, var(--control-mid), var(--control-dark));
  }
  .unlock-knob {
    position: absolute;
    left: 12px;
    top: 16px;
    width: 70px;
    height: 70px;
    border-radius: 50%;
    background: var(--knob-grey);
    display: flex;
    align-items: center;
    justify-content: center;
  }
</style>
</head>
<body>
  <main class="canvas">
    <section class="lock-ad">
      <div class="app-emblem" role="img" aria-label="Space for the app emblem"></div>
      <h1 class="app-title">Quill Puzzles Plus</h1>
      <p class="app-tagline">EXERCISE YOUR BRAIN</p>
      <div class="start-button">Start Now</div>
      <div class="unlock-slider">
        <div class="unlock-knob">
          <svg width="24" height="30" viewBox="0 0 24 30" aria-hidden="true">
            <path d="M6 13 V9 a6 6 0 0 1 12 0 V13" fill="none" stroke="var(--icon-light)" stroke-width="3"/>
            <rect x="3" y="13" width="18" height="15" rx="2" fill="var(--icon-light)"/>
            <circle cx="12" cy="20" r="2.2" fill="var(--knob-grey)"/>
          </svg>
        </div>
      </div>
    </section>
  </main>
</body>
</html>
```